quorvelbank.com

Design proposals for a gold bank site and gold wallet main page. The site will let people (and companies) open accounts and purchase gold for deposit and later make payments with the gold they hold in the bank. The bank will be a e-money licensed venture located in Switzerland. The functionality of the "system" will be very simple and possibly only use icon symbols so it can be multilingual.

The mainstays of the site will be security and trust. Al digital gold is backed 100 % by visible gold in vault audited every day.

Target Market(s)

Asian and American gold buyers and people preferring gold to currency

Industry/Entity Type

Security

Requirements
Must have
• a) Logo
b) Main index page with a new logo and design
c) System (post log in e-wallet) main page showing the last transactions of the client and give client options to transfer funds and make deposits
Nice to have
• sample contact form
sample faq page
terms page design
Should not have
• So much text since it will be aimed at the worldwide market

```html
<!DOCTYPE html>
<html lang="en">
<head>
<meta charset="utf-8">
<title>Quorvel – Safe Place For Your Gold</title>
<link rel="stylesheet" href="https://fonts.googleapis.com/css2?family=Source+Sans+3:wght@400;600&display=swap">
<style>
:root{
  --orange:#f06419;
  --orange-dark:#c94f0c;
  --text:#333;
  --muted:#555;
  --panel:#f6f6f6;
  --panel-inner:#efefef;
  --band:#e4e4e4;
  --line:#d4d4d4;
  --footer:#242424;
  --footer-edge:#5a5a5a;
  --white:#fff;
}
*{box-sizing:border-box;margin:0;padding:0}
html,body{width:1091px;height:1200px;overflow:hidden;background:var(--white)}
body{font-family:"Source Sans 3",Arial,sans-serif;color:var(--text)}
.page{position:relative;width:1000px;height:1100px;transform:scale(1.091);transform-origin:0 0}
.abs{position:absolute}

/* top bar */
.topbar{left:0;top:0;width:1000px;height:34px;background:var(--orange)}
.toplinks{right:175px;top:7px;color:var(--white);font-size:13px;font-weight:600;display:flex;gap:14px}
.toplinks span.sep{font-weight:400}
.search{left:856px;top:4px;width:130px;height:25px;background:var(--white);border:1px solid #d9d9d9;border-radius:3px;font-size:11px;font-style:italic;color:#aaa;padding:5px 8px}
.search svg{position:absolute;right:6px;top:6px}

/* header */
.logo{left:16px;top:52px;font-size:58px;color:var(--orange);letter-spacing:1px;line-height:1}
.tab-active{left:491px;top:37px;width:69px;height:91px;background:linear-gradient(#e4e4e4,#fff 45%)}
.nav{left:509px;top:101px;display:flex;gap:32px;font-size:13px;color:var(--orange)}
.header-rule{left:16px;top:128px;width:971px;height:1px;background:var(--orange)}

/* slider */
.slider{left:16px;top:145px;width:972px;height:293px;border:1px solid var(--line);background:var(--white)}
.slider-shadow{left:16px;top:438px;width:972px;height:14px;background:radial-gradient(ellipse at 50% 0,rgba(0,0,0,.28),rgba(0,0,0,0) 70%)}
.slide{left:30px;top:156px;width:947px;height:272px;background:linear-gradient(#eef0f3,#c9cbd1 55%,#7f818b)}
.slide-photo{left:160px;top:156px;width:340px;height:272px;background:radial-gradient(circle at 50% 50%,#d8d9dc,#a9abb0 60%,#8e9096)}
.slide-caption{left:590px;top:312px;font-size:29px;color:var(--white)}
.arrow{top:276px}

/* welcome */
.welcome-title{left:16px;top:484px;font-size:21px;color:var(--orange)}
.welcome-text{left:16px;top:524px;width:693px;font-size:12.2px;line-height:22px;text-align:justify;color:var(--text)}
.welcome-photo{left:727px;top:494px;width:246px;height:155px;border:1px solid #ddd;padding:3px;background:var(--white);box-shadow:0 1px 3px rgba(0,0,0,.15)}
.welcome-photo div{width:100%;height:100%;background:linear-gradient(135deg,#d9dde2,#b9c3cc 40%,#e7e9ec 70%,#8c969f)}

/* columns */
.col-title{top:688px;font-size:18px;color:var(--orange);display:flex;align-items:center;gap:14px}
.panel{top:724px;height:270px;background:var(--panel);border-radius:4px}
.panel-inner{left:10px;top:11px;bottom:9px;right:10px;background:var(--panel-inner);border-radius:3px;overflow:hidden}
.panel-shadow{top:992px;height:10px;background:radial-gradient(ellipse at 50% 0,rgba(0,0,0,.2),rgba(0,0,0,0) 70%)}
.entry{position:absolute;left:41px;width:232px;font-size:11px;line-height:16px;color:var(--text);text-align:justify}
.entry h3{font-weight:400;font-size:12.5px;color:var(--orange);line-height:16px;margin-bottom:8px;text-align:justify}
.entry h3 .date{color:var(--text)}
.entry .pen{position:absolute;left:-28px;top:2px}
.band{left:0;right:0;bottom:0;height:27px;background:var(--band);text-align:right;padding:5px 17px 0 0;font-size:11.5px}
.band a{color:var(--orange);text-decoration:underline}

/* form */
.form-row{position:absolute;left:17px;font-size:11px;color:var(--muted)}
.field{position:absolute;left:77px;width:199px;height:28px;background:var(--white);border:1px solid #c8c8c8;box-shadow:inset 0 1px 3px rgba(0,0,0,.12)}
.submit{position:absolute;left:193px;top:213px;width:83px;height:25px;border-radius:4px;background:linear-gradient(#f47b2e,var(--orange-dark));color:var(--white);font-size:13px;text-align:center;line-height:25px;box-shadow:0 1px 2px rgba(0,0,0,.3)}

/* footer */
.footer{left:0;top:1022px;width:1000px;height:78px;background:var(--footer);border-top:4px solid var(--footer-edge)}
.footer-links{left:17px;top:1043px;font-size:11.5px;color:#ddd;display:flex;gap:7px}
.footer-links .sep{color:#888}
.copyright{left:17px;top:1069px;font-size:11.5px;color:#bbb}
.social{left:879px;top:1050px;display:flex;gap:12px}
.social span{width:27px;height:27px;border-radius:50%;background:#8a8a8a;display:block}
</style>
</head>
<body>
<div class="page">

  <div class="abs topbar"></div>
  <nav class="abs toplinks"><span>Login</span><span class="sep">|</span><span>Register</span><span class="sep">|</span><span>Help</span></nav>
  <div class="abs search">Search
    <svg width="11" height="11" viewBox="0 0 11 11"><circle cx="4.5" cy="4.5" r="3.3" fill="none" stroke="#bbb" stroke-width="1.4"/><line x1="7" y1="7" x2="10" y2="10" stroke="#bbb" stroke-width="1.6"/></svg>
  </div>

  <div class="abs logo">Quorvel</div>
  <div class="abs tab-active"></div>
  <nav class="abs nav"><span>Home</span><span>About us</span><span>Services</span><span>Deposits</span><span>Testimonials</span><span>Contact us</span></nav>
  <div class="abs header-rule"></div>

  <div class="abs slider"></div>
  <div class="abs slider-shadow"></div>
  <div class="abs slide"></div>
  <div class="abs slide-photo" role="img" aria-label="Steel bank vault door with locking wheel"></div>
  <div class="abs slide-caption">Safe Place For Your Gold</div>
  <svg class="abs arrow" style="left:35px" width="24" height="34" viewBox="0 0 24 34"><polyline points="20,2 4,17 20,32" fill="none" stroke="#fff" stroke-width="3" opacity=".85"/></svg>
  <svg class="abs arrow" style="left:943px" width="24" height="34" viewBox="0 0 24 34"><polyline points="4,2 20,17 4,32" fill="none" stroke="#fff" stroke-width="3" opacity=".85"/></svg>

  <h1 class="abs welcome-title" style="font-weight:400">Welcome to Quorvel</h1>
  <p class="abs welcome-text">Nemo enim ipsam voluptatem quia voluptas sit aspernatur aut odit aut fugit, sed quia consequuntur magni dolores eos qui ratione voluptatem sequi nesciunt. Neque porro quisquam est, qui dolorem ipsum quia dolor sit amet, consectetur, adipisci velit, sed quia non numquam eius modi tempora incidunt ut labore et dolore magnam aliquam quaerat voluptatem. Ut enim ad minima veniam, quis nostrum exercitationem ullam corporis suscipit laboriosam, nisi ut aliquid ex ea commodi consequatur. Quis autem vel eum iure reprehenderit qui in ea voluptate velit esse quam nihil molestiae consequatur, vel illum qui dolorem eum fugiat quo voluptas nulla pariatur.</p>
  <div class="abs welcome-photo"><div role="img" aria-label="Businessman in a white shirt and tie sitting outdoors under a parasol"></div></div>

  <!-- FAQ -->
  <h2 class="abs col-title" style="left:16px;font-weight:400">
    <svg width="27" height="28" viewBox="0 0 27 28"><rect x="2" y="3" width="22" height="23" rx="2" fill="#3d74c2"/><rect x="5" y="6" width="16" height="17" fill="#6fa0e0"/><text x="13" y="21" font-size="16" font-family="Source Sans 3,sans-serif" font-weight="600" fill="#fff" text-anchor="middle">?</text></svg>
    FAQ</h2>
  <div class="abs panel" style="left:14px;width:313px">
    <div class="abs panel-inner">
      <div class="entry" style="top:17px"><svg class="pen" width="17" height="16" viewBox="0 0 17 16"><rect x="1" y="3" width="11" height="12" fill="none" stroke="#888"/><path d="M6 10 L14 2 L16 4 L8 12 L5 13Z" fill="#bbb" stroke="#777"/></svg><h3>Duis aute irure dolor in reprehenderit in voluptate velit esse</h3>Excepteur and sint occaecat cupidatat non proident, sunt in culpa qui officia deserunt mollit anim id est laborum.</div>
      <div class="entry" style="top:128px"><svg class="pen" width="17" height="16" viewBox="0 0 17 16"><rect x="1" y="3" width="11" height="12" fill="none" stroke="#888"/><path d="M6 10 L14 2 L16 4 L8 12 L5 13Z" fill="#bbb" stroke="#777"/></svg><h3>Duis aute irure dolor in reprehenderit in voluptate velit esse</h3>Excepteur and sint occaecat cupidatat non proident, sunt in culpa qui officia deserunt mollit anim id est laborum.</div>
      <div class="abs band"><a>View all</a></div>
    </div>
  </div>
  <div class="abs panel-shadow" style="left:30px;width:280px"></div>

  <!-- Testimonials -->
  <h2 class="abs col-title" style="left:355px;font-weight:400">
    <svg width="31" height="26" viewBox="0 0 31 26"><ellipse cx="15" cy="11" rx="14" ry="10" fill="#d8d8d8" stroke="#aaa"/><path d="M9 19 L7 25 L14 20Z" fill="#d8d8d8" stroke="#aaa"/><text x="15" y="18" font-size="18" font-family="Georgia,serif" fill="#666" text-anchor="middle">“</text></svg>
    Testimonials</h2>
  <div class="abs panel" style="left:345px;width:313px">
    <div class="abs panel-inner">
      <div class="entry" style="top:17px"><svg class="pen" width="17" height="16" viewBox="0 0 17 16"><rect x="1" y="3" width="11" height="12" fill="none" stroke="#888"/><path d="M6 10 L14 2 L16 4 L8 12 L5 13Z" fill="#bbb" stroke="#777"/></svg><h3>Client’s Name <span class="date">August 28th, 2012</span></h3>Excepteur and sint occaecat cupidatat non proident, sunt in culpa qui officia deserunt mollit anim id est laborum inventore veritatis et quasi architecto beatae.</div>
      <div class="entry" style="top:128px"><svg class="pen" width="17" height="16" viewBox="0 0 17 16"><rect x="1" y="3" width="11" height="12" fill="none" stroke="#888"/><path d="M6 10 L14 2 L16 4 L8 12 L5 13Z" fill="#bbb" stroke="#777"/></svg><h3>Client’s Name <span class="date">August 28th, 2012</span></h3>Excepteur and sint occaecat cupidatat non proident, sunt in culpa qui officia deserunt mollit anim id est laborum inventore veritatis et quasi architecto beatae.</div>
      <div class="abs band"><a>View all</a></div>
    </div>
  </div>
  <div class="abs panel-shadow" style="left:361px;width:280px"></div>

  <!-- Contact -->
  <h2 class="abs col-title" style="left:693px;font-weight:400">
    <svg width="28" height="27" viewBox="0 0 28 27"><rect x="1" y="1" width="26" height="25" rx="3" fill="#b8242a"/><path d="M9 6 C7 8 8 13 12 17 C16 21 20 21 21 19 L19 16 L16 17 C14 16 11 13 10 11 L11 8Z" fill="#fff"/></svg>
    Contact us</h2>
  <div class="abs panel" style="left:676px;width:312px">
    <div class="abs panel-inner">
      <div class="form-row" style="top:26px">Name :</div><div class="field" style="top:18px"></div>
      <div class="form-row" style="top:67px">Email :</div><div class="field" style="top:59px"></div>
      <div class="form-row" style="top:108px">Phone :</div><div class="field" style="top:100px"></div>
      <div class="form-row" style="top:149px">Message :</div><div class="field" style="top:141px;height:58px"></div>
      <div class="submit">SUBMIT</div>
    </div>
  </div>
  <div class="abs panel-shadow" style="left:692px;width:280px"></div>

  <!-- footer -->
  <footer class="abs footer"></footer>
  <nav class="abs footer-links"><span>Home</span><span class="sep">|</span><span>About us</span><span class="sep">|</span><span>Services</span><span class="sep">|</span><span>Deposits</span><span class="sep">|</span><span>Testimonials</span><span class="sep">|</span><span>Contact us</span><span class="sep">|</span><span>Sign in</span><span class="sep">|</span><span>Register</span><span class="sep">|</span><span>Help</span></nav>
  <div class="abs copyright">Copyright © 2012 www.quorvelbank.com &nbsp;&nbsp; All rights reserved.</div>
  <div class="abs social"><span aria-label="Social network link"></span><span aria-label="Social network link"></span><span aria-label="Social network link"></span></div>

</div>
</body>
</html>
```